Video Editing Website - Wordpress Design Project

Hi There
I am setting up a Tribute Funeral Video and Home Video Editing Website for my Company. "Reel Keepsake". This is to assist people with putting together their Videos and Photos with music to show at a Funeral or for Family Memories. I already have a domain www.reelkeepsake.com.au, but I have no host yet.

Some websites that already do this are http://www.lanternclips.com.au/tributes, http://www.hearthfilmcraft.com.au/services/funeral-tribute-videos.html, and http://www.quillmontage.com.au/
These are examples not to cpy, but to get an idea of what I am offering so you can design accordingly.

I have a logo which is attached. You will see that the logo is mainly blue, so I would appreciate a website with that colour on the pages, but not ALL over the page.

I would like to upload videos occasionally from flickstow.com so I would appreciate that option incorporated.

Thank you lots.
Callum

Target Market(s)

Families predominately in the 25-60 age range

Industry/Entity Type

It Company

Requirements
Must have
• *Ability to upload Videos from flickstow.com
*Ability for me to edit the content whenever I need to
*A contact page to send email messages to me

```html
<!DOCTYPE html>
<html lang="en">
<head>
<meta charset="utf-8">
<title>Reel Keepsake</title>
<link href="https://fonts.googleapis.com/css2?family=Ubuntu:wght@300;400;500;700&family=Arimo:wght@400;700&display=swap" rel="stylesheet">
<style>
:root{
  --brand-blue:#1e4fa8;
  --hero-top:#1f3fa6;
  --hero-mid:#2a64cf;
  --link-blue:#1f74c4;
  --ink:#111111;
  --upload:#44a700;
  --gallery:#e2005a;
  --tips:#00bde5;
  --panel:#e9e9e9;
  --field-border:#c9c9c9;
  --subscribe:#d8131b;
  --footer:#2e2e2e;
  --footer-bottom:#1f1f1f;
  --footer-text:#6f6f6f;
}
*{box-sizing:border-box;margin:0;padding:0}
html,body{width:826px;height:1200px;overflow:hidden;background:#fff}
body{position:relative;font-family:"Ubuntu",sans-serif;color:var(--ink)}
.abs{position:absolute}

/* header */
.brand{left:32px;top:27px;white-space:nowrap}
.brand-mark{width:54px;height:54px;border-radius:50%;background:var(--brand-blue);margin:0 0 14px 34px}
.brand-name{font-weight:400;font-size:24px;color:var(--brand-blue);line-height:1;white-space:nowrap}
.brand-tag{font-family:"Arimo",sans-serif;font-size:6.5px;color:#333;margin-top:3px}
.account{left:626px;top:49px;font-family:"Arimo",sans-serif;font-size:9.5px;color:#111}
.account-row{display:flex;align-items:center;height:14px;margin-bottom:6px}
.account-row svg{width:11px;height:11px;margin-right:10px}
.account-row b{font-weight:700;letter-spacing:.3px}
.search-box{width:146px;height:17px;border:1px solid #bcbcbc}

.main-nav{left:0;width:826px;top:171px;display:flex;justify-content:center;font-family:"Arimo",sans-serif;font-weight:700;font-size:13px}
.main-nav a{color:var(--ink);text-decoration:none;padding:0 18px;position:relative}
.main-nav a.active{color:var(--link-blue)}
.main-nav a+a::before{content:"|";position:absolute;left:-3px;color:var(--ink)}

/* hero */
.hero{left:32px;top:227px;width:762px;height:316px;background:linear-gradient(180deg,var(--hero-top) 0%,var(--hero-mid) 55%,var(--hero-top) 100%)}
.hero-title{left:33px;top:28px;color:#fff;font-weight:500;font-size:29px;line-height:1;white-space:nowrap}
.hero-sub{left:33px;top:60px;color:#fff;font-weight:500;font-size:15px;white-space:nowrap}
.hero-copy{left:33px;top:104px;width:210px;color:#fff;font-size:9.3px;line-height:11.8px;text-align:justify}
.hero-dots{left:33px;top:274px;display:flex;gap:7px}
.hero-dots span{width:12px;height:12px;background:#fff}
.hero-more{left:169px;top:268px;width:66px;height:24px;border-radius:6px;background:#0b0b0b;color:#fff;font-family:"Arimo",sans-serif;font-size:9.5px;display:flex;align-items:center;justify-content:center}
.player{left:277px;top:32px;width:456px;height:255px;background:#000}
.player-frame{position:absolute;left:0;top:31px;width:456px;height:193px;background:linear-gradient(180deg,#d6d2cc 0%,#a8a49c 50%,#3e3b36 100%)}
.player-actions{position:absolute;right:4px;top:4px;display:flex;flex-direction:column;gap:3px}
.player-actions span{width:20px;height:16px;background:#1a1a1a;border-radius:2px}
.player-bar{position:absolute;left:0;bottom:0;width:456px;height:31px;display:flex;align-items:center;padding:0 10px;gap:10px}
.track{flex:1;height:5px;border:1px solid #444;position:relative}
.track i{position:absolute;left:0;top:0;height:3px;width:28px;background:#2a8de0}
.hd{color:#2a8de0;font:700 8px "Arimo",sans-serif}

/* tiles */
.tile{top:584px;width:227px;height:51px;color:#fff;font-weight:500;font-size:20px;display:flex;align-items:center;justify-content:center;letter-spacing:.3px}
.tile-upload{left:32px;background:var(--upload)}
.tile-gallery{left:300px;background:var(--gallery)}
.tile-tips{left:567px;background:var(--tips)}

/* welcome */
.welcome{left:32px;top:672px;width:494px}
.welcome h2{font-weight:500;font-size:18.5px;padding-bottom:10px;border-bottom:1px solid #222;margin-bottom:14px}
.welcome p{font-weight:300;font-size:11.2px;line-height:17.8px;letter-spacing:-.1px;text-align:justify;margin-bottom:18px;color:#111}

/* newsletter */
.newsletter{left:567px;top:676px;width:227px;height:265px;background:var(--panel);border-radius:4px;font-family:"Arimo",sans-serif}
.nl-brand{position:absolute;left:18px;top:14px;white-space:nowrap}
.nl-brand .brand-mark{width:30px;height:30px;margin:0 0 6px 18px}
.nl-brand .brand-name{font-family:"Ubuntu",sans-serif;font-size:12px}
.nl-heading{position:absolute;left:99px;top:40px;font-weight:700;font-size:11.5px;color:#222;white-space:nowrap}
.nl-copy{position:absolute;left:18px;top:84px;width:195px;font-size:10px;line-height:10.5px;color:#222}
.field{position:absolute;left:18px;width:191px;height:17px;background:#fff;border:1px solid var(--field-border);font-size:8.8px;color:#555;padding:3px 6px}
.nl-more{position:absolute;left:26px;top:237px;font-size:9.5px;color:#222}
.subscribe{position:absolute;left:143px;top:226px;width:64px;height:21px;background:var(--subscribe);color:#fff;font-size:9.5px;display:flex;align-items:center;justify-content:center}

/* footer */
.site-footer{left:0;top:986px;width:826px;height:171px;background:var(--footer)}
.foot-col{position:absolute;top:28px}
.foot-col h3{font-weight:400;font-size:13.5px;color:#e6e6e6;margin-bottom:8px;letter-spacing:.2px}
.foot-col li{list-style:none;font-size:9px;line-height:19.5px;color:var(--footer-text)}
.foot-col li.current{color:#fff}
.copyright{left:0;top:1157px;width:826px;height:43px;background:var(--footer-bottom);color:#b5b5b5;font-family:"Arimo",sans-serif;font-size:10px;display:flex;align-items:center;justify-content:center}
</style>
</head>
<body>

<header>
  <div class="abs brand">
    <div class="brand-mark"></div>
    <div class="brand-name">Reel Keepsake</div>
    <div class="brand-tag">Relive Your Memories</div>
  </div>

  <div class="abs account">
    <div class="account-row">
      <svg viewBox="0 0 12 12"><circle cx="6" cy="3.5" r="3" fill="#111"/><path d="M0 12c0-4 3-5 6-5s6 1 6 5z" fill="#111"/></svg>
      Welcome ( log in ) | Sign Up
    </div>
    <div class="account-row">
      <svg viewBox="0 0 12 12"><path d="M1.5 7V6a4.5 4.5 0 0 1 9 0v1" fill="none" stroke="#111" stroke-width="1.4"/><rect x="0.5" y="6.5" width="3" height="5" rx="1" fill="#111"/><rect x="8.5" y="6.5" width="3" height="5" rx="1" fill="#111"/></svg>
      Happy to help&nbsp;<b>0400 318 275</b>
    </div>
    <div class="account-row">
      <svg viewBox="0 0 12 12"><circle cx="5" cy="5" r="3.5" fill="none" stroke="#111" stroke-width="1.6"/><path d="M7.5 7.5l3.5 3.5" stroke="#111" stroke-width="1.8"/></svg>
      <span class="search-box"></span>
    </div>
  </div>

  <nav class="abs main-nav">
    <a class="active">HOME</a><a>PACKAGE</a><a>GALLERY</a><a>SERVICES</a><a>TIPS</a><a>CONTACT US</a>
  </nav>
</header>

<section class="abs hero">
  <h1 class="abs hero-title">Share and store</h1>
  <div class="abs hero-sub">your memories with us</div>
  <p class="abs hero-copy">Lorem Ipsum is simply dummy text of the printing and typesetting industry. Lorem Ipsum has been the industry's standard dummy text ever since the 1500s, when an unknown printer took a galley of type and scrambled it to make a type specimen book. It has survived not only five centuries, but also the leap into electronic typesetting, remaining essentially unchanged. It was popularised in the 1960s with the release of Typeplate sheets containing L</p>
  <div class="abs hero-dots"><span></span><span></span><span></span><span></span></div>
  <div class="abs hero-more">MORE</div>

  <div class="abs player">
    <div class="player-frame" role="img" aria-label="Video still of a street lined with tall palm trees under a hazy sky"></div>
    <div class="player-actions"><span></span><span></span><span></span></div>
    <div class="player-bar">
      <svg width="10" height="10" viewBox="0 0 10 10"><rect x="1" y="1" width="3" height="8" fill="#fff"/><rect x="6" y="1" width="3" height="8" fill="#fff"/></svg>
      <div class="track"><i></i></div>
      <span class="hd">IIIIII HD</span>
    </div>
  </div>
</section>

<a class="abs tile tile-upload">UPLOAD</a>
<a class="abs tile tile-gallery">GALLERY</a>
<a class="abs tile tile-tips">TIPS</a>

<section class="abs welcome">
  <h2>Welcome to Reel Keepsake</h2>
  <p>Lorem Ipsum is simply dummy text of the printing and typesetting industry. Lorem Ipsum has been the industry's standard dummy text ever since the 1500s, when an unknown printer took a galley of type and scrambled it to make a type specimen book. It has survived not only five centuries, but also the leap into electronic typesetting, remaining essentially unchanged. It was popularised in the 1960s with the release of Typeplate sheets containing Lorem Ipsum passages, and more recently with desktop publishing software like Pagecraft including versions of Lorem Ipsum. m</p>
  <p>Text ever since the 1500s, when an unknown printer took a galley of type and scrambled it to make a type specimen book. It has survived not only five centuries, but also the leap into electronic typesetting, remaining essentially unchanged. It was popularised in the 1960s with the release of Typeplate sheets containing Lorem Ipsum passages, and more recently with desktop publishing software like Pagecraft including versions of Lorem Ipsum.</p>
</section>

<aside class="abs newsletter">
  <div class="nl-brand">
    <div class="brand-mark"></div>
    <div class="brand-name">Reel Keepsake</div>
  </div>
  <div class="nl-heading">STAY CONNECTED</div>
  <p class="nl-copy">Sign up for our newsletter and receive our best deals in your inbox.</p>
  <div class="field" style="top:126px">Name</div>
  <div class="field" style="top:159px">Email</div>
  <div class="field" style="top:191px">Contact Number</div>
  <div class="nl-more">More about it</div>
  <div class="subscribe">Subscribe</div>
</aside>

<footer class="abs site-footer">
  <div class="foot-col" style="left:100px">
    <h3>QUICK LINKS</h3>
    <ul><li class="current">Full Service Solution</li><li>ClipPlan</li><li>ClipLease</li><li>Design &amp; Installation</li><li>Video Panels</li></ul>
  </div>
  <div class="foot-col" style="left:269px">
    <h3>BUSINESS</h3>
    <ul><li>Full Service Solution</li><li>ClipPlan</li><li>ClipLease</li><li>Design &amp; Installation</li><li>Video Panels</li></ul>
  </div>
  <div class="foot-col" style="left:441px">
    <h3>SERVICES</h3>
    <ul><li>Full Service Solution</li><li>ClipPlan</li><li>ClipLease</li><li>Design &amp; Installation</li><li>Video Panels</li></ul>
  </div>
  <div class="foot-col" style="left:611px">
    <h3>CONTACT</h3>
    <ul><li>Full Service Solution</li><li>ClipPlan</li><li>ClipLease</li><li>Design &amp; Installation</li><li>Video Panels</li></ul>
  </div>
</footer>
<div class="abs copyright">Copyright Brightway Studio 2014. All rights reserved.</div>

</body>
</html>
```